New Business Card for chocolate Company

I am looking to have business cards for my Chocolate Company Velvet Spoon Sweets.
I hand make all organic, fair trade, vegan, gluten free, allergy friendly chocolate. We are located in Austin Texas and are very Proud to be a locally made good. I have my logo and new sticker design for our boxes but now I need cards. I was thinking either natural craft or white. But I want to have a bit of funk to the cards so someone will hold onto it for a long time.
The important info is
Dora Pennweather
Owner and Chocolatier
Velvet Spoon Sweets
velvetspoonsweetsatx.example
velvetspoonsweets@mailbox.example
velvetspoonsweets on instagram
512.555.0183

Velvet Spoon sweets are Vegan ,Gluten free, organic, fair trade, allergy friendly hand made chocolate.

Target Market(s)

We cater to all ages. Our chocolate is on the higher price scale and is a decadent treat. But we make custom molds for any event kids party's to an elegant wedding.

Industry/Entity Type

Business

Requirements
Must have
• Good design logo and some sort of austin vibe.

```html
<!DOCTYPE html>
<html lang="en">
<head>
<meta charset="utf-8">
<title>Velvet Spoon Sweets – Business Card</title>
<link rel="stylesheet" href="https://fonts.googleapis.com/css2?family=Oswald:wght@400;600&family=Raleway:wght@300&display=swap">
<style>
  :root {
    --backdrop: #d9d7d4;
    --cocoa: #3a2a24;
    --cocoa-light: #5a4238;
    --truffle: #4a3129;
    --mint: #a8d8da;
    --paper: #ffffff;
    --paper-tint: #efedec;
    --ink: #2a1e1a;
    --ink-soft: #5b514d;
    --rule: #8b817d;
  }
  * { box-sizing: border-box; margin: 0; padding: 0; }
  html, body { width: 1200px; height: 748px; overflow: hidden; }
  body {
    background: var(--backdrop);
    position: relative;
    font-family: "Oswald", sans-serif;
  }

  /* ---------- Front of card ---------- */
  .card-front {
    position: absolute;
    left: 80px; top: 220px;
    width: 540px; height: 309px;
    background: var(--cocoa);
    box-shadow: 0 10px 24px rgba(0,0,0,.25);
  }
  .photo-tile {
    position: absolute;
    width: 120px; height: 86px;
    border: 5px solid var(--paper);
    background: linear-gradient(135deg, var(--cocoa-light), var(--truffle) 60%, #e8e4e0);
  }
  .photo-tile--top { left: 342px; top: 22px; }
  .photo-tile--bottom { left: 78px; top: 200px; }
  .brand-tile {
    position: absolute;
    left: 190px; top: 104px;
    width: 160px; height: 102px;
    background: var(--mint);
    border: 5px solid var(--paper);
    display: flex; align-items: center; justify-content: center;
  }
  .brand-name {
    font-family: "Oswald", sans-serif;
    font-weight: 600;
    color: var(--ink);
    text-transform: uppercase;
    text-align: center;
    font-size: 20px;
    line-height: 1.05;
    letter-spacing: 1px;
  }

  /* ---------- Back of card ---------- */
  .card-back {
    position: absolute;
    left: 760px; top: 104px;
    width: 309px; height: 540px;
    background: var(--paper);
    padding: 16px;
    box-shadow: 0 10px 24px rgba(0,0,0,.2);
  }
  .card-back__field {
    width: 100%; height: 100%;
    background: var(--paper-tint);
    display: flex; flex-direction: column; align-items: center;
    padding-top: 42px;
  }
  .brand-tile--small {
    position: static;
    width: 124px; height: 82px;
    border-width: 4px;
  }
  .brand-tile--small .brand-name { font-size: 16px; }
  .rule {
    width: 196px;
    border-top: 2px dotted var(--rule);
  }
  .rule--above { margin-top: 52px; }
  .person-name {
    margin-top: 10px;
    font-weight: 600;
    font-size: 21px;
    letter-spacing: 1px;
    color: var(--ink);
    text-transform: uppercase;
  }
  .person-title {
    font-family: "Raleway", sans-serif;
    font-weight: 300;
    font-size: 15px;
    color: var(--ink-soft);
    margin: 2px 0 10px;
  }
  .phone {
    margin-top: 20px;
    font-weight: 600;
    font-size: 22px;
    letter-spacing: 1px;
    color: var(--ink);
  }
  .contact-list {
    list-style: none;
    margin-top: 22px;
    text-align: center;
    font-size: 11px;
    letter-spacing: 2px;
    text-transform: uppercase;
    color: var(--ink);
    line-height: 1.45;
  }
  .contact-list .gap { margin-top: 10px; }
</style>
</head>
<body>

  <section class="card-front" aria-label="Card front">
    <div class="photo-tile photo-tile--top" role="img" aria-label="Photo of heart-shaped chocolates on a white plate"></div>
    <div class="brand-tile">
      <span class="brand-name">Velvet Spoon<br>Sweets</span>
    </div>
    <div class="photo-tile photo-tile--bottom" role="img" aria-label="Photo of decorated chocolate squares"></div>
  </section>

  <section class="card-back" aria-label="Card back">
    <div class="card-back__field">
      <div class="brand-tile brand-tile--small">
        <span class="brand-name">Velvet Spoon<br>Sweets</span>
      </div>
      <div class="rule rule--above"></div>
      <h1 class="person-name">Dora Pennweather</h1>
      <p class="person-title">Owner and Chocolatier</p>
      <div class="rule"></div>
      <p class="phone">512-555-0183</p>
      <ul class="contact-list">
        <li>Instagram</li>
        <li>velvetspoonsweets</li>
        <li class="gap">info@velvetspoonsweetsatx.example</li>
        <li>velvetspoonsweets@mailbox.example</li>
      </ul>
    </div>
  </section>

</body>
</html>
```